Flyer für ein Jugendfestival
Zielgruppe
Wir sind ein christlicher Jugendverband, der hauptsächlich Freizeiten organisiert. Die Haupt-Zielgruppe sind somit Jugendliche im Alter von 13-17 Jahre, darüber hinaus junge Erwachsene im Alter von 18-25. Viele haben einen christlichen Kontext, viele allerdings nicht. Gemein haben alle, dass sie im Sommer unterwegs waren.
Aufgabenstellung
Der Flyer ist für das 'Grasp the Lantern', unser Jugendfestival, dieses findet vom 15.-17. September 2023 statt. Motto: 'hier da.heim' Ort: Lindenbrück. Preis: 74€. Alter: ab 13 Jahre.
Mögliche Farbgebung in Richtung: rosa, flieder, blau oder grün (nicht allzu bunt, farblich stimmig). Inhaltlicher Schwerpunkt ist Sicherheit, muss aber nicht wörtlich vorkommen.
Es müssen keine realen Bilder vorkommen, sondern gern auch nur Silhouetten oder Farbverläufe...
Idee für die Aufteilung: Vorderseite: Daten, Rückseite: Aktionen und Teaser der Bands (Workshops, Jesus erleben, Worship, Lounge, Döner, Funkenhain-Ensemble, Morgen wird bunter... ) Kann aber auch abweichen, da gerade noch nicht alle Acts feststehen
Somit soll der Flyer für Jugendliche ansprechend wirken, möglichst alle repräsentieren (also nicht nur eine Person, sondern mehrere oder gar keine), 'in sein' und mit dem Trend gehen.

```html
<!DOCTYPE html>
<html lang="de">
<head>
<meta charset="utf-8">
<title>Grasp the Lantern – Flyer</title>
<link rel="stylesheet" href="https://fonts.googleapis.com/css2?family=Barlow+Condensed:wght@400;500;700;800&family=Oswald:wght@400;500;600&display=swap">
<style>
  :root{
    --stage:#727272;
    --white:#ffffff;
    --orange:#e8771f;
    --ink:#3a1f5c;
    --lilac-1:#f1ddf0;
    --lilac-2:#b8a2e0;
    --violet:#6a3fae;
    --ice:#cfe9f5;
    --blue:#8c9fe0;
  }
  *{box-sizing:border-box;margin:0;padding:0}
  html,body{width:1200px;height:848px;overflow:hidden;background:var(--stage)}
  .stage{position:relative;width:1200px;height:848px}
  .flyer{position:absolute;top:70px;width:360px;height:722px;overflow:hidden}
  .flyer--front{left:349px}
  .flyer--back{left:774px}
  .flyer__art{position:absolute;inset:0}
  .flyer__art--front{
    background:
      radial-gradient(ellipse 60% 30% at 20% 55%, var(--ice) 0%, transparent 70%),
      radial-gradient(ellipse 50% 25% at 80% 20%, var(--lilac-1) 0%, transparent 70%),
      radial-gradient(ellipse 60% 25% at 40% 85%, var(--lilac-1) 0%, transparent 70%),
      radial-gradient(ellipse 40% 30% at 75% 45%, var(--violet) 0%, transparent 70%),
      linear-gradient(160deg, var(--lilac-2) 0%, var(--blue) 45%, var(--violet) 70%, var(--lilac-2) 100%);
  }
  .flyer__art--back{
    background:
      radial-gradient(ellipse 60% 25% at 55% 20%, var(--lilac-1) 0%, transparent 70%),
      radial-gradient(ellipse 50% 20% at 70% 50%, var(--ice) 0%, transparent 70%),
      radial-gradient(ellipse 50% 25% at 20% 40%, var(--violet) 0%, transparent 70%),
      radial-gradient(ellipse 60% 25% at 40% 90%, var(--lilac-1) 0%, transparent 70%),
      linear-gradient(170deg, var(--lilac-2) 0%, var(--violet) 40%, var(--blue) 70%, var(--lilac-2) 100%);
  }
  .flyer__type{position:absolute;inset:0;width:360px;height:722px}
  .t-cond{font-family:"Barlow Condensed",sans-serif}
  .t-display{font-family:"Oswald",sans-serif}
  .program{position:absolute;right:42px;top:468px;text-align:right;
    font-family:"Barlow Condensed",sans-serif;font-weight:400;font-size:21px;line-height:26.7px;color:var(--white)}
  .contact{position:absolute;right:42px;top:612px;text-align:right;
    font-family:"Barlow Condensed",sans-serif;font-weight:400;font-size:13px;line-height:18px;color:var(--white)}
  .contact__label{color:var(--ink)}
  .social{position:absolute;right:42px;top:668px;
    font-family:"Barlow Condensed",sans-serif;font-weight:400;font-size:13px;color:var(--white)}
</style>
</head>
<body>
<main class="stage">

  <section class="flyer flyer--front">
    <div class="flyer__art flyer__art--front" role="img" aria-label="Abstrakte fließende 3D-Wellen in Flieder, Rosa und Eisblau"></div>
    <svg class="flyer__type" viewBox="0 0 360 722" xmlns="http://www.w3.org/2000/svg">
      <text class="brand t-cond" transform="translate(68 118) rotate(-90)" font-weight="800" font-size="30" fill="#222">Weitblick</text>

      <text class="title-main t-display" transform="translate(253 467) rotate(-90)" font-weight="500" font-size="160" fill="var(--white)" textLength="390" lengthAdjust="spacingAndGlyphs">GRASP</text>
      <text class="title-sub t-display" x="24" y="243" font-weight="500" font-size="60" fill="var(--orange)" textLength="315" lengthAdjust="spacing">THE LANTERN</text>

      <text class="date-month t-cond" transform="translate(49 557) rotate(-90)" font-weight="500" font-size="19" fill="var(--white)" letter-spacing="0.5">september 2023</text>
      <text class="date-day t-display" x="36" y="632" font-weight="400" font-size="76" fill="var(--white)">15</text>
      <rect class="date-dash" x="117" y="604" width="12" height="4" fill="var(--white)"/>
      <text class="date-day t-display" x="36" y="702" font-weight="400" font-size="76" fill="var(--white)">17.</text>

      <text class="motto t-cond" x="142" y="634" font-weight="500" font-size="42" fill="var(--white)" textLength="183" lengthAdjust="spacing">hier da.heim</text>
      <text class="details t-cond" x="142" y="661" font-weight="500" font-size="12" fill="var(--white)" textLength="186" lengthAdjust="spacing">Lindenbrück | ab 13 Jahre | Preis: 74€</text>
    </svg>
  </section>

  <section class="flyer flyer--back">
    <div class="flyer__art flyer__art--back" role="img" aria-label="Abstrakte fließende 3D-Wellen in Flieder, Violett und Hellblau"></div>
    <svg class="flyer__type" viewBox="0 0 360 722" xmlns="http://www.w3.org/2000/svg">
      <text class="motto-vertical t-cond" transform="translate(81 313) rotate(-90)" font-weight="500" font-size="58" fill="var(--orange)" textLength="246" lengthAdjust="spacingAndGlyphs">hier da.heim</text>
      <g class="arrows" fill="none" stroke="var(--ink)" stroke-width="5" stroke-linejoin="miter">
        <polyline points="124,76 148,90 124,104"/>
        <polyline points="156,76 180,90 156,104"/>
      </g>
    </svg>
    <p class="program">
      workshops | jesus erleben<br>
      worship | lounge | döner<br>
      Funkenhain-Ensemble<br>
      morgen wird bunter...uvm...
    </p>
    <p class="contact">
      <span class="contact__label">infos &amp; anmeldung unter:</span><br>
      jonas beispiel | 0987 65432 | kontakt@jonas-beispiel.de
    </p>
    <p class="social">find us @weitblick.jugend</p>
  </section>

</main>
</body>
</html>
```